Brindle Advisory Business Card Design

Business card for business consulting company, using attached logo. We do financial and strategic consulting, and want a clean, professional image with a bit of fun. Our logo is a flat whale tail, which symbolizes the Orca whale, a highly collaborative, group based animal that is very successful in navigating the ocean, protecting the herd, and hunting. We like the logo that is blue and gray on white one one side, but would be open to a blue card with white lettering on the other side... or whatever you'd suggest
Updates
Hi all - I have had the logo modified to take the shadowing off the tail. I will post it on the brief... under a file name called updated logo. thank you Added Saturday, April 25, 2015
Target Market(s)
Small to medium sized businesses ($10M to $500M in revenue per year), financial and sales executives, general managers, attorneys and CPAs
Industry/Entity Type
Financial
Contact Information for Business Card
Want company name, contact info - name, title, telephone, email, website, linkedin, twitter and Facebook. No physical address yet.
Requirements
Must have
- contemporary design, bold, strong, confident but with a bit of fun. prominently feature the logo and the whale tail icon
Nice to have
- unique touches that would differentiate us from a regular card... for example, logo and writing all on front on white background, but on back - logo in white on a blue background
- open to idea of different shapes of card than standard... but not sure
Should not have
- ?

```html
<!DOCTYPE html>
<html lang="en">
<head>
<meta charset="utf-8">
<title>Brindle Advisory – Business Card</title>
<link href="https://fonts.googleapis.com/css2?family=Open+Sans:wght@300;400;600;700&display=swap" rel="stylesheet">
<style>
  :root {
    --navy: #0e3b6e;
    --navy-soft: #174a82;
    --white: #ffffff;
    --grey: #7d8590;
    --stage: #e9eaec;
  }
  * { box-sizing: border-box; margin: 0; padding: 0; }
  html, body { width: 1200px; height: 873px; overflow: hidden; }
  body {
    background: var(--stage);
    font-family: "Open Sans", Arial, sans-serif;
    display: flex; align-items: center; justify-content: center; gap: 44px;
  }
  .card {
    position: relative; width: 520px; height: 300px; overflow: hidden;
    box-shadow: 0 2px 10px rgba(0,0,0,.12);
  }

  /* Front */
  .card--front { background: var(--white); }
  .brand { position: absolute; display: flex; align-items: center; gap: 10px; z-index: 2; }
  .brand__mark { width: 30px; height: 30px; border-radius: 5px; background: var(--navy); }
  .brand__name { font-size: 30px; font-weight: 400; letter-spacing: -.5px; line-height: 1; white-space: nowrap; }
  .brand__tag { position: absolute; font-size: 10px; color: var(--navy); z-index: 2; white-space: nowrap; }
  .card--front .brand { left: 34px; top: 32px; }
  .card--front .brand__name { color: var(--navy); }
  .card--front .brand__tag { left: 258px; top: 70px; }

  .person { position: absolute; right: 50px; top: 108px; text-align: right; z-index: 3; }
  .person__name { font-size: 15px; font-weight: 700; letter-spacing: 1.5px; color: var(--navy); line-height: 20px; white-space: nowrap; }
  .person__title { font-size: 12px; color: var(--grey); line-height: 18px; margin-top: 2px; }

  .contact-band {
    position: absolute; left: 0; right: 0; bottom: 0; height: 92px;
    background: var(--navy); color: var(--white); font-size: 11.5px; z-index: 1;
  }
  .contact-list { position: absolute; left: 26px; top: 14px; list-style: none; line-height: 20px; }
  .contact-list li { display: flex; align-items: center; gap: 8px; white-space: nowrap; }
  .contact-list svg { width: 11px; height: 11px; fill: var(--white); flex: none; }
  .address { position: absolute; left: 230px; top: 24px; line-height: 20px; font-style: normal; white-space: nowrap; }
  .band-accent { position: absolute; right: 40px; top: -40px; width: 90px; height: 90px;
    border-radius: 50%; background: var(--navy); border: 7px solid var(--white); }

  /* Back */
  .card--back { background: var(--navy); }
  .back-halo { position: absolute; left: 230px; top: -40px; width: 300px; height: 300px;
    border-radius: 50%; background: var(--navy-soft); }
  .card--back .brand { left: 120px; top: 112px; }
  .card--back .brand__mark { background: transparent; border: 2px solid var(--white); }
  .card--back .brand__name { color: var(--white); }
  .card--back .brand__tag { left: 300px; top: 150px; color: var(--white); }
  .web { position: absolute; left: 40px; top: 232px; font-size: 10px; letter-spacing: 3px; color: var(--white); z-index: 2; white-space: nowrap; }
</style>
</head>
<body>
  <section class="card card--front" aria-label="Business card front">
    <div class="brand">
      <span class="brand__mark"></span>
      <span class="brand__name">Brindle Advisory</span>
    </div>
    <span class="brand__tag">business consulting</span>

    <div class="person">
      <p class="person__name">DANA WHITFIELD</p>
      <p class="person__title">Manager</p>
    </div>

    <div class="contact-band">
      <ul class="contact-list">
        <li><svg viewBox="0 0 12 12"><path d="M2 1h3l1 3-2 1a7 7 0 0 0 3 3l1-2 3 1v3a1 1 0 0 1-1 1A10 10 0 0 1 1 2a1 1 0 0 1 1-1z"/></svg>5550 1827</li>
        <li><svg viewBox="0 0 12 12"><path d="M3 0h6a1 1 0 0 1 1 1v10a1 1 0 0 1-1 1H3a1 1 0 0 1-1-1V1a1 1 0 0 1 1-1zm0 2v7h6V2z"/></svg>555 019 3364</li>
        <li><svg viewBox="0 0 12 12"><path d="M0 2h12v8H0zm1 1v.5l5 3.5 5-3.5V3z"/></svg>dana@brindleadvisory.com</li>
      </ul>
      <address class="address">118 Harbor Point Lane<br>Lakeview, OR 97630</address>
      <span class="band-accent"></span>
    </div>
  </section>

  <section class="card card--back" aria-label="Business card back">
    <span class="back-halo"></span>
    <div class="brand">
      <span class="brand__mark"></span>
      <span class="brand__name">Brindle Advisory</span>
    </div>
    <span class="brand__tag">business consulting</span>
    <p class="web">www.brindleadvisory.com</p>
  </section>
</body>
</html>
```